Income Tax and Accounting Brochure

I need a brochure using my new logo (file attached). I do tax work and accounting work. I am an EA (QDX Enrolled Agent - logo attached) and would like this incorporated into the brochure. I also have a MSA in Accounting. Please incorporate the text that I have provided in the brochure.

Target Market(s)

Tax Clients - both business and individuals

Industry/Entity Type

Accounting

Colors
0054AA
0677BA
7BADD7
CADEEF
E8F1F8

Requirements
Must have
• Use my logo and the QDX EA file in the brochure
Nice to have
• I would like to see a brochure that I can customize with my own text if possible.

```html
<!DOCTYPE html>
<html lang="en">
<head>
<meta charset="utf-8">
<title>Northvale Accounting &amp; Consulting – Trifold Brochure</title>
<link rel="stylesheet" href="https://fonts.googleapis.com/css2?family=Ubuntu:wght@400;500;700&family=PT+Sans:wght@400;700&family=Roboto+Condensed:wght@400;700&display=swap">
<style>
  :root {
    --crimson: #c10b32;
    --wine: #7c1d56;
    --violet: #4a2a80;
    --royal: #0d47a8;
    --brand-blue: #0054aa;
    --sky: #7badd7;
    --mist: #cadeef;
    --ice: #e8f1f8;
    --ink: #3b3b45;
    --paper: #ffffff;
    --stage: #e9ebef;
    --panel-w: 280px;
    --panel-h: 650px;
  }
  * { box-sizing: border-box; margin: 0; padding: 0; }
  html, body { width: 1200px; height: 1200px; overflow: hidden; }
  body {
    background: var(--stage);
    font-family: "PT Sans", Arial, sans-serif;
    color: var(--ink);
    position: relative;
  }
  .sheet {
    position: absolute;
    top: 275px;
    left: 20px;
    display: flex;
    gap: 40px;
  }
  .spread { display: flex; box-shadow: 0 6px 24px rgba(0,0,0,.18); }
  .panel {
    width: var(--panel-w);
    height: var(--panel-h);
    position: relative;
    overflow: hidden;
  }
  .eyebrow {
    font-family: "Ubuntu", sans-serif;
    font-weight: 500;
    font-size: 12px;
    color: var(--crimson);
    text-transform: uppercase;
    text-align: center;
  }
  .headline {
    font-family: "Ubuntu", sans-serif;
    font-weight: 500;
    font-size: 18px;
    line-height: 1.15;
    color: #3a3a44;
    text-transform: uppercase;
    text-align: center;
    margin-top: 4px;
  }
  .rule {
    width: 90px; height: 2px; background: var(--brand-blue);
    margin: 8px auto 0;
  }
  .copy {
    font-size: 10.5px;
    line-height: 1.6;
    text-align: justify;
    color: #4a4a55;
  }
  .copy + .copy { margin-top: 10px; }

  /* Left inside panel */
  .panel-why { background: linear-gradient(180deg, #ececee 0%, #f6f6f7 45%, #fff 100%); }
  .panel-why::before {
    content: ""; position: absolute; left: 0; top: 0; bottom: 0; width: 8px;
    background: linear-gradient(180deg, var(--crimson), var(--violet) 55%, var(--royal));
  }
  .panel-why .intro { padding: 30px 24px 0 32px; }
  .photo-advisor {
    position: absolute; left: 8px; right: 0; top: 140px; height: 170px;
    background: linear-gradient(120deg, #d9dde3 0%, #eef0f3 45%, #c9cfd8 100%);
  }
  .panel-why .body {
    position: absolute; left: 8px; right: 0; top: 290px; bottom: 0;
    background: #fff;
    border-top-left-radius: 0;
    padding: 26px 22px 0 26px;
  }
  .panel-why .body::before {
    content: ""; position: absolute; left: 0; right: 0; top: -24px; height: 30px;
    background: #fff;
    transform: skewY(-5deg); transform-origin: left;
  }
  .section-title {
    font-family: "Ubuntu", sans-serif; font-weight: 500;
    font-size: 18px; color: var(--crimson); text-align: center; text-transform: uppercase;
    position: relative;
  }
  .section-sub {
    font-family: "Ubuntu", sans-serif; font-weight: 500;
    font-size: 13px; color: var(--brand-blue); text-align: center; text-transform: uppercase;
    margin: 2px 0 12px;
  }

  /* Middle inside panel */
  .panel-benefits {
    background: linear-gradient(160deg, var(--crimson) 0%, var(--wine) 30%, var(--violet) 62%, var(--royal) 100%);
    color: #fff;
    padding: 40px 22px 0 24px;
  }
  .panel-benefits .eyebrow { color: #fff; font-size: 11px; }
  .panel-benefits .headline { color: #fff; font-size: 19px; }
  .panel-benefits .rule { background: #fff; width: 100px; }
  .timeline { position: relative; margin-top: 38px; padding-left: 56px; }
  .timeline::before {
    content: ""; position: absolute; left: 18px; top: -8px; bottom: -20px; width: 1.5px;
    background: rgba(255,255,255,.85);
  }
  .timeline::after {
    content: ""; position: absolute; left: 14px; bottom: -26px; width: 9px; height: 9px;
    border-radius: 50%; background: #fff;
  }
  .benefit { position: relative; padding-top: 8px; margin-bottom: 22px; border-top: 1px dotted rgba(255,255,255,.5); }
  .benefit-icon {
    position: absolute; left: -56px; top: 10px; width: 38px; height: 38px;
    border-radius: 50%; background: #fff;
    display: flex; align-items: center; justify-content: center;
  }
  .benefit h3 {
    font-family: "Ubuntu", sans-serif; font-weight: 500; font-size: 12.5px;
    text-transform: uppercase; letter-spacing: .2px; margin-bottom: 4px;
  }
  .benefit p { font-size: 10px; line-height: 1.55; color: rgba(255,255,255,.92); text-align: justify; }

  /* Right inside panel */
  .panel-books { background: linear-gradient(180deg, #fff 0%, #f4f4f5 100%); padding: 44px 24px 0; }
  .panel-books .copy { margin-top: 22px; }
  .photo-paperwork {
    position: absolute; left: 0; right: 0; bottom: 0; height: 300px;
    background: linear-gradient(180deg, #f4f4f5 0%, #dcdcde 40%, #c6c7ca 100%);
  }

  /* Front cover */
  .panel-cover {
    background: var(--paper);
    box-shadow: 0 6px 24px rgba(0,0,0,.18);
    text-align: center;
  }
  .brand { padding-top: 44px; display: flex; flex-direction: column; align-items: center; }
  .brand-dot { width: 66px; height: 66px; border-radius: 50%; background: var(--brand-blue); }
  .brand-name {
    font-family: "Ubuntu", sans-serif; font-weight: 500; color: var(--brand-blue);
    font-size: 17px; line-height: 1.3; margin-top: 18px; letter-spacing: .5px;
  }
  .cover-arc { position: absolute; left: 0; top: 180px; width: 280px; height: 120px; }
  .photo-consultants {
    position: absolute; left: 10px; right: 0; top: 215px; height: 260px;
    background: linear-gradient(180deg, #e8f1f8 0%, #9fb3cf 35%, #2f3f66 75%, #f5f7fa 100%);
    border-top-left-radius: 140px 60px; border-top-right-radius: 140px 60px;
  }
  .tagline-top {
    position: absolute; left: 0; right: 0; top: 506px;
    font-family: "Roboto Condensed", sans-serif; font-size: 17px; color: var(--crimson);
    text-transform: uppercase;
  }
  .tagline-main {
    position: absolute; left: 0; right: 0; top: 530px;
    font-family: "Roboto Condensed", sans-serif; font-weight: 700; font-size: 30px;
    color: var(--brand-blue); text-transform: uppercase;
  }
  .cover-band {
    position: absolute; left: 0; right: 0; bottom: 0; height: 10px;
    background: linear-gradient(90deg, var(--crimson), var(--royal));
  }
</style>
</head>
<body>
<main class="sheet">
  <section class="spread" aria-label="Brochure inside spread">
    <article class="panel panel-why">
      <div class="intro">
        <p class="eyebrow">What a joy</p>
        <h2 class="headline">It is to watch<br>success in action!</h2>
        <div class="rule"></div>
      </div>
      <div class="photo-advisor" role="img" aria-label="Photo of a smiling accountant at his desk"></div>
      <div class="body">
        <h2 class="section-title">Tax Preparation</h2>
        <p class="section-sub">Why hire us?</p>
        <p class="copy">Preparing your own income tax return can be a task that leaves you with more questions than answers. According to a study released by the National Filing Review Office last year, most taxpayers (77% of 71 million taxpayers) believe they benefited from using a professional tax preparer.</p>
        <p class="copy">Whether we like it or not, today's tax laws are so complicated that filing a relatively simple return can be confusing. It is just too easy to overlook deductions and credits to which you are entitled. Even if you use a computer software program there's no substitute for the assistance of an experienced tax professional.</p>
      </div>
    </article>

    <article class="panel panel-benefits">
      <p class="eyebrow">Here's</p>
      <h2 class="headline">What your get...</h2>
      <div class="rule"></div>
      <div class="timeline">
        <div class="benefit">
          <span class="benefit-icon"><svg width="20" height="20" viewBox="0 0 20 20" fill="none" stroke="#3b3f8f" stroke-width="1.4"><rect x="4" y="2" width="12" height="16" rx="1"/><path d="M7 13v-3M10 13V7M13 13v-5"/></svg></span>
          <h3>Rechecked return file</h3>
          <p>Your tax return will be checked and rechecked by our computer software identifying potential problems the QDX may look at more closely and reviewing the math to limit QDX contacts.</p>
        </div>
        <div class="benefit">
          <span class="benefit-icon"><svg width="20" height="20" viewBox="0 0 20 20" fill="none" stroke="#3b3f8f" stroke-width="1.4"><rect x="4" y="2" width="12" height="16" rx="1"/><path d="M7 6h6M7 9h6M7 12h4"/></svg></span>
          <h3>Filed electronically</h3>
          <p>Your tax return can be filed electronically so you will get a refund back quicker.</p>
        </div>
        <div class="benefit">
          <span class="benefit-icon"><svg width="20" height="20" viewBox="0 0 20 20" fill="none" stroke="#3b3f8f" stroke-width="1.4"><rect x="2" y="6" width="13" height="8" rx="1"/><circle cx="14" cy="13" r="4"/><path d="M14 11v4"/></svg></span>
          <h3>Money back</h3>
          <p>Our staff will show you how to adjust your payroll withholding to get more money back each week. Why give the QDX an interest free loan for up to 16 months.</p>
        </div>
        <div class="benefit">
          <span class="benefit-icon"><svg width="20" height="20" viewBox="0 0 20 20" fill="none" stroke="#3b3f8f" stroke-width="1.4"><rect x="4" y="2" width="12" height="16" rx="1"/><path d="M7 7l6 6M13 7l-6 6"/></svg></span>
          <h3>Potential deductions</h3>
          <p>We will show you potential deductions to limit your tax liability for next year. In addition, we will give you a sheet of commonly overlooked deductions to lower the following year's tax liability.</p>
        </div>
      </div>
    </article>

    <article class="panel panel-books">
      <p class="eyebrow">Books a mess</p>
      <h2 class="headline">No problem!</h2>
      <div class="rule"></div>
      <p class="copy">If you own a small business and haven't kept up your bookkeeping, don't worry. We can help you. We'll prepare your bookkeeping for the year, prepare a full Schedule C, as well as your personal income tax return. Then we'll help you set up an easy system that allows you to keep your books in tip-top shape next year.</p>
      <div class="photo-paperwork" role="img" aria-label="Black and white photo of hands reviewing paperwork with a pen"></div>
    </article>
  </section>

  <article class="panel panel-cover" aria-label="Brochure front cover">
    <div class="brand">
      <span class="brand-dot"></span>
      <p class="brand-name">NORTHVALE ACCOUNTING<br>&amp; CONSULTING, LLC</p>
    </div>
    <svg class="cover-arc" viewBox="0 0 280 120" aria-hidden="true"><path d="M20 120 Q140 -20 260 110" fill="none" stroke="var(--mist)" stroke-width="10"/></svg>
    <div class="photo-consultants" role="img" aria-label="Photo of two business consultants reviewing a tablet together"></div>
    <p class="tagline-top">Forming foundation for</p>
    <p class="tagline-main">Business Growth</p>
    <div class="cover-band"></div>
  </article>
</main>
</body>
</html>
```